Need design for Vinyl window signs

I need Vinyl window sign to cover my front retail pharmacy window. Not the whole window area i want there to be open areas so people can still see inside.
Attached is the pic of front door and also the logo which contains the colors we want to use. The width of the door is about 14ft wide and 7ft high and its 3 sections. The middle section the door is 36 inch.

And the vinyl graphic should include the following info:
Maplecrest Commons pharmacy
Caring for you, Caring for the community

Wellness starts here!
Locally owned independent pharmacy
No wait
Same Copay as chains
Free local delivery

We do prescriptions, private consultations, compounding, immunizations, travel health and other clinical services

We also provide free blood pressure, blood glucose and blood oxygen testing everyday.
No appointments necessary.

Write Pharmacy in different languages: Spanish, Farsi, Hebrew, Russian

Phone: 555-206-3948

Hours:
M- F 9-6
Sat and sun and major Holliday: closed

Target Market(s)

Patients: People seeking medication or health advice. Caregivers: Those caring for others who need prescriptions. Health-Conscious Individuals: People interested in preventive health measures. Chronic Condition Sufferers: Individuals managing ongoing health issues. Healthcare Professionals: Doctors and nurses who may refer patients to pharmacists.

Industry/Entity Type

Retail pharmacy

Font styles to use
Sans Serif

Colors
0054AA
0677BA
7BADD7
CADEEF
E8F1F8
00AB8E
00BBA5
67D7C9
C6EFE9
E9F9F6

Requirements
Must have
• At least 3 sections for each window left side and right side and middle area, must have Green and blue color to match my logo see attached.
Nice to have
• Like to see a pics or two of people maybe seniors and younger adults enjoying their time

```html
<!DOCTYPE html>
<html lang="en">
<head>
<meta charset="utf-8">
<title>Maplecrest Commons Pharmacy – Window Signs</title>
<link rel="stylesheet" href="https://fonts.googleapis.com/css2?family=Montserrat:wght@500;600;700;800&family=Noto+Serif:ital,wght@1,700&family=Noto+Sans+Arabic:wght@600&family=Noto+Sans+Hebrew:wght@600&display=swap">
<style>
  :root {
    --blue: #0677ba;
    --blue-deep: #0054aa;
    --green: #0bb04b;
    --white: #ffffff;
    --backdrop: #333335;
  }
  * { margin: 0; padding: 0; box-sizing: border-box; }
  html, body { width: 732px; height: 1200px; overflow: hidden; }
  body {
    background: var(--backdrop);
    font-family: "Montserrat", sans-serif;
    position: relative;
  }
  .sign {
    position: absolute;
    left: 26px;
    width: 680px;
    height: 385px;
    overflow: hidden;
  }
  .sign > * { position: absolute; white-space: nowrap; }
  .sign-wellness { top: 201px; background: var(--green); }
  .sign-offers { top: 614px; background: var(--green); }

  .band-blue { left: 0; top: 0; width: 680px; background: var(--blue); }
  .sign-wellness .band-blue { height: 243px; }
  .sign-offers .band-blue { top: 281px; height: 104px; }

  /* Headline */
  .headline-box {
    top: 29px; height: 52px;
    font-weight: 800; font-size: 38px; line-height: 52px;
  }
  .headline-wellness { left: 41px; width: 261px; background: var(--white); color: var(--blue-deep); text-align: center; }
  .headline-starts { left: 302px; width: 336px; background: var(--green); color: var(--white); text-align: center; }

  /* Services */
  .service { display: flex; align-items: center; gap: 9px; }
  .service-icon { width: 38px; height: 38px; flex: none; }
  .service-label {
    color: var(--white); font-weight: 600; font-size: 16.5px; line-height: 19px;
  }

  .tagline {
    left: 122px; top: 225px; width: 434px; height: 37px;
    background: var(--white); border-radius: 19px;
    font-family: "Noto Serif", serif; font-style: italic; font-weight: 700;
    font-size: 19px; line-height: 37px; text-align: center;
    color: var(--blue-deep);
  }

  /* Phone */
  .phone-pill {
    left: 55px; top: 298px; width: 313px; height: 47px;
    background: var(--white); border-radius: 24px;
    padding-left: 60px;
    font-weight: 800; font-size: 29px; line-height: 47px;
    color: var(--blue-deep); letter-spacing: -0.5px;
  }
  .phone-badge { left: 41px; top: 292px; width: 60px; height: 60px; }

  /* Hours */
  .hours-frame {
    left: 402px; top: 289px; width: 236px; height: 79px;
    border: 1.5px solid var(--white); border-radius: 6px;
  }
  .hours-label {
    left: 435px; top: 276px; width: 172px; height: 24px;
    background: var(--blue); color: var(--white);
    font-weight: 700; font-size: 15px; line-height: 24px; text-align: center;
    border-radius: 3px;
  }
  .hours-text {
    left: 402px; top: 306px; width: 236px;
    color: var(--white); font-weight: 500; font-size: 12.5px; line-height: 15.5px;
    text-align: center;
  }
  .hours-text b { font-weight: 800; }

  /* Offers */
  .tag {
    font-weight: 800; font-size: 36px; line-height: 50px; padding-left: 12px;
    height: 50px; letter-spacing: -0.3px;
  }
  .tag-white { background: var(--white); color: var(--blue-deep); }
  .tag-blue { background: var(--blue); color: var(--white); }
  .tag-free-delivery { left: 33px; top: 29px; width: 134px; }
  .tag-delivery { left: 33px; top: 81px; width: 231px; }
  .tag-free-testing { left: 387px; top: 29px; width: 134px; }
  .tag-testings { left: 387px; top: 81px; width: 230px; }

  .fact {
    font-weight: 700; font-size: 22px; line-height: 31px; color: var(--white);
  }
  .fact-highlight { background: var(--blue); padding: 0 10px; display: inline-block; }
  .fact-owned { left: 33px; top: 153px; }
  .fact-independent { left: 43px; top: 185px; font-weight: 600; }
  .fact-copay { left: 33px; top: 226px; }

  .testing-frame {
    left: 370px; top: 106px; width: 276px; height: 141px;
    border: 1.5px solid var(--white); border-radius: 8px;
  }
  .testing-list { left: 387px; top: 142px; list-style: none; }
  .testing-list li {
    display: flex; align-items: center; gap: 6px;
    color: var(--white); font-weight: 700; font-size: 19px; line-height: 30px;
  }
  .tick { width: 12px; height: 12px; flex: none; }

  .language-pill {
    top: 311px; width: 132px; height: 42px;
    background: var(--white); border-radius: 21px;
    color: var(--blue); font-weight: 700; font-size: 18px; line-height: 42px;
    text-align: center;
    box-shadow: 0 2px 3px rgba(0,0,0,0.25);
  }
  .lang-es { left: 33px; }
  .lang-fa { left: 193px; font-family: "Noto Sans Arabic", sans-serif; font-weight: 600; }
  .lang-he { left: 353px; font-family: "Noto Sans Hebrew", sans-serif; font-weight: 600; }
  .lang-ru { left: 512px; }
</style>
</head>
<body>

<section class="sign sign-wellness" aria-label="Wellness services sign">
  <div class="band-blue"></div>
  <div class="headline-box headline-wellness">WELLNESS</div>
  <div class="headline-box headline-starts">STARTS HERE!</div>

  <div class="service" style="left:33px; top:94px;">
    <svg class="service-icon" viewBox="0 0 38 38"><circle cx="13" cy="26" r="11" fill="#0bb04b"/><rect x="13" y="5" width="15" height="20" rx="1.5" fill="none" stroke="#fff" stroke-width="1.6"/><path d="M16 10h5M16 14h9M16 18h6" stroke="#fff" stroke-width="1.4"/><path d="M32 12l-8 14" stroke="#fff" stroke-width="1.8"/></svg>
    <span class="service-label">Prescriptions</span>
  </div>
  <div class="service" style="left:33px; top:134px;">
    <svg class="service-icon" viewBox="0 0 38 38"><circle cx="13" cy="26" r="11" fill="#0bb04b"/><circle cx="28" cy="9" r="4" fill="none" stroke="#fff" stroke-width="1.5"/><circle cx="18" cy="17" r="4" fill="none" stroke="#fff" stroke-width="1.5"/><circle cx="24" cy="29" r="4" fill="none" stroke="#fff" stroke-width="1.5"/><path d="M21 15l4-4M20 21l3 4" stroke="#fff" stroke-width="1.5"/></svg>
    <span class="service-label">Compounding</span>
  </div>
  <div class="service" style="left:33px; top:174px;">
    <svg class="service-icon" viewBox="0 0 38 38"><circle cx="13" cy="26" r="11" fill="#0bb04b"/><path d="M21 6l9 3v9c0 7-5 11-9 13-4-2-9-6-9-13V9z" fill="none" stroke="#fff" stroke-width="1.6"/><path d="M21 14v9M16.5 18.5h9" stroke="#fff" stroke-width="1.6"/></svg>
    <span class="service-label">Immunizations</span>
  </div>

  <div class="service" style="left:226px; top:96px;">
    <svg class="service-icon" viewBox="0 0 38 38"><circle cx="13" cy="27" r="11" fill="#0bb04b"/><rect x="11" y="9" width="16" height="20" rx="2" fill="none" stroke="#fff" stroke-width="1.6"/><path d="M16 9V5h6v4M15 13v12M19 13v12M23 13v12" stroke="#fff" stroke-width="1.4"/><path d="M29 20l5 2v4c0 3-2 5-5 6-3-1-5-3-5-6v-4z" fill="#0677ba" stroke="#fff" stroke-width="1.4"/></svg>
    <span class="service-label">Travel<br>Health Services</span>
  </div>
  <div class="service" style="left:226px; top:164px;">
    <svg class="service-icon" viewBox="0 0 38 38"><circle cx="13" cy="27" r="11" fill="#0bb04b"/><rect x="13" y="6" width="17" height="23" rx="1.5" fill="none" stroke="#fff" stroke-width="1.6"/><path d="M17 12h9M17 16h9M17 20h6" stroke="#fff" stroke-width="1.4"/><path d="M27 30l-4-4a2.5 2.5 0 014-3 2.5 2.5 0 014 3z" fill="#0677ba" stroke="#fff" stroke-width="1.3"/></svg>
    <span class="service-label">Other<br>Clinical Services</span>
  </div>

  <div class="service" style="left:436px; top:96px;">
    <svg class="service-icon" viewBox="0 0 38 38"><circle cx="13" cy="27" r="11" fill="#0bb04b"/><circle cx="14" cy="22" r="7" fill="none" stroke="#fff" stroke-width="1.5"/><text x="14" y="26" font-size="10" fill="#fff" text-anchor="middle" font-family="Montserrat, sans-serif">?</text><rect x="20" y="6" width="14" height="11" rx="5" fill="#0677ba" stroke="#fff" stroke-width="1.5"/><path d="M24 10h6M24 13h5" stroke="#fff" stroke-width="1.2"/></svg>
    <span class="service-label">Private<br>Consultations</span>
  </div>
  <div class="service" style="left:436px; top:166px;">
    <svg class="service-icon" viewBox="0 0 38 38"><circle cx="13" cy="27" r="11" fill="#0bb04b"/><rect x="12" y="8" width="22" height="21" rx="2" fill="none" stroke="#fff" stroke-width="1.6"/><path d="M12 14h22M17 5v5M29 5v5" stroke="#fff" stroke-width="1.5"/><path d="M19 25c0-5 1-7 4-7s4 2 4 7zM22 27h2" stroke="#fff" stroke-width="1.3" fill="none"/></svg>
    <span class="service-label">No appointments<br>necessary</span>
  </div>

  <div class="tagline">Caring for you,Caring for the community</div>

  <div class="phone-pill">555-206-3948</div>
  <svg class="phone-badge" viewBox="0 0 60 60" aria-hidden="true">
    <circle cx="30" cy="30" r="29" fill="#fff"/>
    <circle cx="30" cy="30" r="25" fill="#0677ba"/>
    <path d="M22 17c2-1 3 0 4 2l2 4c0 2-2 3-2 4 1 3 4 6 7 7 1 0 2-2 4-2l4 2c2 1 3 2 2 4-1 3-4 4-6 4-9-1-17-9-18-18 0-3 1-6 3-7z" fill="none" stroke="#fff" stroke-width="1.8"/>
    <path d="M33 19a9 9 0 017 7M33 14a14 14 0 0112 12" fill="none" stroke="#fff" stroke-width="1.6"/>
  </svg>

  <div class="hours-frame"></div>
  <div class="hours-label">OPENING HOURS</div>
  <div class="hours-text">
    Monday - Friday : <b>9:00 - 6:00</b><br>
    Saturday &amp; Sunday<br>
    and Major Holliday : <b>Closed</b>
  </div>
</section>

<section class="sign sign-offers" aria-label="Free delivery and testing sign">
  <div class="band-blue"></div>

  <div class="tag tag-white tag-free-delivery">FREE</div>
  <div class="tag tag-blue tag-delivery">DELIVERY</div>

  <div class="fact fact-owned"><span class="fact-highlight">LOCALLY OWNED</span></div>
  <div class="fact fact-independent">Independent Pharmacy</div>
  <div class="fact fact-copay"><span class="fact-highlight">SAME COPAY</span> as chains</div>

  <div class="testing-frame"></div>
  <div class="tag tag-white tag-free-testing">FREE</div>
  <div class="tag tag-blue tag-testings">TESTINGS</div>
  <ul class="testing-list">
    <li><svg class="tick" viewBox="0 0 12 12"><circle cx="6" cy="6" r="6" fill="#0677ba"/><path d="M3.3 6.2l1.8 1.8 3.6-3.8" fill="none" stroke="#fff" stroke-width="1.4"/></svg>Blood Pressure</li>
    <li><svg class="tick" viewBox="0 0 12 12"><circle cx="6" cy="6" r="6" fill="#0677ba"/><path d="M3.3 6.2l1.8 1.8 3.6-3.8" fill="none" stroke="#fff" stroke-width="1.4"/></svg>Blood Glucose Testing</li>
    <li><svg class="tick" viewBox="0 0 12 12"><circle cx="6" cy="6" r="6" fill="#0677ba"/><path d="M3.3 6.2l1.8 1.8 3.6-3.8" fill="none" stroke="#fff" stroke-width="1.4"/></svg>Blood Oxygen Testing</li>
  </ul>

  <div class="language-pill lang-es" lang="es">farmacia</div>
  <div class="language-pill lang-fa" lang="fa" dir="rtl">داروخانه</div>
  <div class="language-pill lang-he" lang="he" dir="rtl">בֵּית מִרְקַחַת</div>
  <div class="language-pill lang-ru" lang="ru">Аптека</div>
</section>

</body>
</html>
```